Food company needs to improve packaging design

Objective:
We are looking for a graphic designer to help improve and elevate the design of our tortilla chips packaging. We’ve created a draft version that we will provide as a reference, but we’re open to creative input and fresh ideas to make the design more appealing and shelf-ready.

Scope of Work:

Redesign the front of the packaging, with room for creative freedom.

You may change the background, colors, and overall layout if you believe it enhances the design.

The back of the packaging should remain unchanged, but you are welcome to propose minor visual tweaks if necessary for consistency.

Design Goals:

Create a bold, appealing design that stands out on shelves.

Maintain clarity and readability of all key product information.

Reflect a fresh, natural, and high-quality product image.

Deliverables:

Print-ready files (preferably AI or PSD with layers).

High-resolution mockups.

Any font files or external assets used.

Additional Notes:

We’re open to different design directions, so feel free to explore concepts.

We will need to finish writing the copy for the back, but we have already created some space for it. Please do not remove the space.

We have attached the branding guide, but we have freedom on the font for the packaging. We have also attached a different packaging to show that we don't necessarily have to use the colors from our branding guide for the background. However, if you decide to go away from our colors, please choose them carefully and provide another design option with our green as the background to compare.

You will also find the blank die line cut to work on your design.

Please ensure that the design remains practical for commercial printing and meets basic packaging guidelines.

```html
<!DOCTYPE html>
<html lang="en">
<head>
<meta charset="utf-8">
<title>Nuvo Snacks – Keto Low Carb Tortilla Chips</title>
<link rel="stylesheet" href="https://fonts.googleapis.com/css2?family=Lilita+One&family=Montserrat:wght@500;600;700;800&display=swap">
<style>
  :root {
    --backdrop: #7fa656;
    --bag-red: #a8414f;
    --bag-red-deep: #8c3341;
    --bag-red-light: #c2525f;
    --lime: #a8d66f;
    --lime-bright: #8ed14b;
    --white: #ffffff;
    --pink: #cf5a6c;
    --seal-red: #b3303f;
    --photo-dark: #4a4a4f;
    --photo-wood: #a97b4d;
    --photo-chip: #d2b47a;
    --ink-maroon: #6b1f2a;
  }
  * { margin: 0; padding: 0; box-sizing: border-box; }
  html, body { width: 1200px; height: 960px; overflow: hidden; background: var(--backdrop); }
  .canvas { position: relative; width: 1200px; height: 960px; }
  .bag {
    position: absolute; left: 358px; top: 139px; width: 484px; height: 682px;
    overflow: hidden;
    background: radial-gradient(ellipse at 45% 35%, var(--bag-red-light), var(--bag-red) 55%, var(--bag-red-deep));
  }
  .bag-art { position: absolute; inset: 0; }
  .crimp { position: absolute; left: 0; right: 0; height: 14px;
    background: repeating-linear-gradient(to bottom, rgba(0,0,0,.14) 0 1px, transparent 1px 3px); }
  .crimp--top { top: 0; }
  .crimp--bottom { bottom: 0; }
  .brand { position: absolute; left: 206px; top: 46px; width: 126px; text-align: center; color: var(--lime); font-family: "Montserrat", sans-serif; font-weight: 800; }
  .brand__name { font-size: 36px; line-height: 40px; letter-spacing: 2px; }
  .brand__sub { font-size: 11.5px; letter-spacing: 2.4px; line-height: 16px; }
  .claim-keto { position: absolute; left: 82px; top: 112px; font: 700 36px/40px "Montserrat", sans-serif; color: var(--white); }
  .headline { position: absolute; font-family: "Lilita One", sans-serif; color: var(--lime); line-height: 1; letter-spacing: 1px; }
  .headline--low { left: 82px; top: 152px; font-size: 74px; }
  .headline--carb { left: 88px; top: 222px; font-size: 90px; }
  .product-type { position: absolute; left: 92px; top: 306px; font: 700 28px/34px "Montserrat", sans-serif; color: var(--white); letter-spacing: .5px; }
  .natural-badge { position: absolute; left: 262px; top: 145px; width: 82px; height: 76px; }
  .natural-badge__text { position: absolute; left: 4px; top: 33px; width: 60px; text-align: center; font: 800 8.5px/10px "Montserrat", sans-serif; color: var(--white); }
  .flavour { position: absolute; left: 247px; top: 361px; width: 144px; height: 144px; border-radius: 50%;
    background: var(--pink); border: 5px solid var(--white); text-align: center; padding-top: 46px; }
  .flavour__name { font: 27px/30px "Lilita One", sans-serif; color: var(--lime); letter-spacing: 1px; }
  .flavour__note { font: 700 15px/18px "Montserrat", sans-serif; color: var(--white); letter-spacing: .5px; }
  .seal { position: absolute; left: 155px; top: 566px; width: 48px; height: 48px; border-radius: 50%;
    background: var(--seal-red); border: 3px solid var(--white); }
  .net-weight { position: absolute; left: 100px; top: 617px; width: 160px; text-align: center; font: 500 11px/14px "Montserrat", sans-serif; color: var(--white); }
  .less-calories { position: absolute; left: 112px; top: 638px; width: 134px; height: 16px; background: var(--white); text-align: center;
    font: 700 9.5px/16px "Montserrat", sans-serif; color: var(--ink-maroon); }
</style>
</head>
<body>
<main class="canvas">
  <section class="bag" aria-label="Tortilla chips bag front">
    <svg class="bag-art" viewBox="0 0 484 682" width="484" height="682">
      <defs>
        <linearGradient id="photoTone" x1="0" y1="0" x2="1" y2="1">
          <stop offset="0" stop-color="var(--photo-wood)"/>
          <stop offset="0.4" stop-color="var(--photo-dark)"/>
          <stop offset="0.7" stop-color="var(--photo-chip)"/>
          <stop offset="1" stop-color="#b8955c"/>
        </linearGradient>
      </defs>
      <polygon class="green-field" points="0,682 0,600 484,250 484,682" fill="var(--lime-bright)"/>
      <polygon class="photo" role="img" aria-label="Photo of salsa in a white bowl on a slate and wood board with a pile of tortilla chips" points="40,682 40,560 250,405 484,300 484,682" fill="url(#photoTone)"/>
    </svg>
    <div class="crimp crimp--top"></div>
    <div class="crimp crimp--bottom"></div>

    <div class="brand">
      <div class="brand__name">NUVO</div>
      <div class="brand__sub">SNACKS</div>
    </div>

    <div class="claim-keto">KETO</div>
    <div class="headline headline--low">LOW</div>
    <div class="headline headline--carb">CARB</div>

    <div class="natural-badge">
      <svg width="82" height="76" viewBox="0 0 82 76">
        <path d="M60 14 A28 28 0 1 1 22 12" fill="none" stroke="var(--white)" stroke-width="2.5"/>
        <path d="M54 26 C44 22 40 10 44 2 C54 6 58 16 54 26 Z" fill="var(--white)"/>
        <path d="M56 28 C58 18 68 12 78 12 C76 22 66 30 56 28 Z" fill="var(--white)"/>
      </svg>
      <div class="natural-badge__text">NATURAL<br>100%</div>
    </div>

    <div class="product-type">TORTILLA CHIPS</div>

    <div class="flavour">
      <div class="flavour__name">SEA SALT</div>
      <div class="flavour__note">FAT-FREE</div>
    </div>

    <div class="seal" aria-hidden="true"></div>
    <div class="net-weight">Net Wt. 8 oz (244g)</div>
    <div class="less-calories">81% Less Calories</div>
  </section>
</main>
</body>
</html>
```